■依頼の目的/概要
鶏白湯塩ラーメンのポスター作成お願いします!

■依頼詳細
鶏白湯塩ラーメンのポスターを作成お願いします。
値段は780円です。

デザインについては特に、指定はありません。
A1のポスターです。

鶏白湯塩ラーメンについて

鶏白湯スープにじっくり時間をかけて熟成させた自家製塩タレを合わせ、アクセントにアオサを使用しました。
(こちらの文章を入れて欲しいです。)

写真はURLからダウンロードお願いします。

http://filebako.example/dl/7a1c93e0b5d2f4c8a6e1027b3d9f5c4e8a1b6d20

お店のイメージです。
こちらのお店の物になります。

https://gurumemo.example/fukuoka/B7002/B700209/51178364/

https://www.tomobook.example/torisoba.hakata/
http://filebako.example/dl/3e8d21f6c0a94b7e5d13a8f2c6b0e974d1a5c3b8

おそくなりましたこちらからダウンロードお願いしいます。
再度アップしました。こちらからダウンロードできますか?
http://filebako.example/dl/c5b07e3a91d6f2e48a0c7b15d3e9f6a2b4c81d07

とても素晴らしいデザインありがとうございます!

提案ありがとうございました!

```html
<!DOCTYPE html>
<html lang="ja">
<head>
<meta charset="utf-8">
<title>熟成 鶏白湯塩</title>
<link rel="stylesheet" href="https://fonts.googleapis.com/css2?family=Yuji+Boku&family=Noto+Serif+JP:wght@500;700&family=Noto+Sans+JP:wght@700;900&display=swap">
<style>
  :root {
    --wood-dark: #1f120b;
    --wood-mid: #4a2c1a;
    --wood-warm: #6b3f22;
    --bowl-white: #ecebe6;
    --bowl-shade: #c9c4ba;
    --title-white: #ffffff;
    --accent-red: #6e1a12;
    --badge-orange: #e9782b;
    --text-white: #ffffff;
  }
  * { margin: 0; padding: 0; box-sizing: border-box; }
  html, body {
    width: 848px; height: 1200px; overflow: hidden;
    background: var(--wood-dark);
  }
  .poster {
    position: relative;
    width: 848px; height: 1200px;
    overflow: hidden;
  }
  .poster__photo {
    position: absolute; inset: 0;
    background:
      radial-gradient(ellipse 640px 420px at 440px 1080px, var(--bowl-white) 0%, var(--bowl-shade) 55%, rgba(201,196,186,0) 75%),
      linear-gradient(180deg, var(--wood-dark) 0%, var(--wood-mid) 45%, var(--wood-warm) 65%, var(--wood-mid) 100%);
  }
  .headline-aged {
    position: absolute;
    left: 560px; top: 44px;
    font-family: "Yuji Boku", serif;
    font-size: 120px;
    font-weight: 400;
    line-height: 1;
    color: var(--accent-red);
    letter-spacing: -2px;
    white-space: nowrap;
    text-shadow: 0 0 6px rgba(255,255,255,0.35);
  }
  .headline-dish {
    position: absolute;
    left: 362px; top: 165px;
    writing-mode: vertical-rl;
    white-space: nowrap;
    font-family: "Yuji Boku", serif;
    font-size: 168px;
    line-height: 1;
    letter-spacing: -6px;
    color: var(--title-white);
    text-shadow: 0 4px 12px rgba(0,0,0,0.45);
  }
  .description {
    position: absolute;
    left: 190px; top: 58px;
    writing-mode: vertical-rl;
    white-space: nowrap;
    font-family: "Noto Serif JP", serif;
    font-weight: 700;
    font-size: 18px;
    line-height: 42px;
    color: var(--text-white);
    text-shadow: 0 1px 4px rgba(0,0,0,0.6);
  }
  .price-badge {
    position: absolute;
    left: 10px; top: 590px;
    width: 186px; height: 186px;
    border-radius: 50%;
    background: var(--badge-orange);
    color: var(--text-white);
    font-family: "Noto Sans JP", sans-serif;
    display: flex; flex-direction: column;
    align-items: center; justify-content: center;
  }
  .price-badge__name { font-size: 15px; font-weight: 700; margin-bottom: 2px; }
  .price-badge__amount { font-size: 54px; font-weight: 900; line-height: 1; }
  .price-badge__unit { font-size: 26px; font-weight: 900; }
</style>
</head>
<body>
  <main class="poster">
    <div class="poster__photo" role="img" aria-label="木目のテーブルに置かれた白い丼の鶏白湯塩ラーメン。白濁スープ、チャーシュー、白髪ねぎ、アオサ、箸で持ち上げた麺"></div>

    <h1 class="headline-aged">熟成</h1>
    <p class="headline-dish">鶏白湯塩</p>

    <p class="description">鶏白湯スープにじっくり時間をかけて<br>熟成させた自家製塩タレを合わせ<br>アクセントにアオサを使用しました。</p>

    <div class="price-badge">
      <span class="price-badge__name">鶏白湯塩ラーメン</span>
      <span class="price-badge__amount">780<span class="price-badge__unit">円</span></span>
    </div>
  </main>
</body>
</html>
```